Poster for a series of live music events

Looking for a simplistic poster design for live music gigs. I would like something that i can reuse by moving the positioning of the words on the poster and the colour scheme. Attached is an example of a design that i like. The size should be A4.
File format preferred would be photoshop.
Text in the poster is not that important at this stage as it is just a template i am after. But it should include band names, location, date and time. So feel free to make up the text. The file provided in the brief will show you the similar things that will be included.
Events

```html
<!DOCTYPE html>
<html lang="en">
<head>
<meta charset="utf-8">
<title>Live Music Gigs Poster</title>
<link rel="stylesheet" href="https://fonts.googleapis.com/css2?family=Teko:wght@400;500&family=Oswald:wght@700&display=swap">
<style>
  :root {
    --bg-dark: #1c262c;
    --bg-mid: #2b3a42;
    --yellow: #f6c619;
    --yellow-light: #ffe03a;
    --yellow-deep: #f0a81a;
    --ink: #111111;
    --white: #ffffff;
  }
  * { margin: 0; padding: 0; box-sizing: border-box; }
  html, body { width: 848px; height: 1200px; overflow: hidden; }
  body {
    position: relative;
    background:
      radial-gradient(ellipse at 50% 40%, var(--bg-mid) 0%, var(--bg-dark) 70%, #141b1f 100%);
    font-family: "Teko", "Arial Narrow", sans-serif;
    color: var(--white);
  }
  .centered { position: absolute; left: 0; width: 848px; text-align: center; line-height: 1; }
  .event-date {
    top: 48px; font-size: 86px; font-weight: 400;
    letter-spacing: 6px; color: var(--yellow);
  }
  .doors {
    top: 162px; font-size: 38px; font-weight: 400;
    letter-spacing: 5px; color: var(--white);
  }
  .emblem { position: absolute; left: 176px; top: 221px; width: 512px; height: 512px; }
  .venue-name {
    top: 448px; font-size: 66px; font-weight: 500;
    letter-spacing: 2px; color: var(--ink);
  }
  .bar {
    position: absolute; left: 124px; width: 620px;
    background: linear-gradient(90deg, var(--yellow-deep), var(--yellow-light) 50%, var(--yellow-deep));
  }
  .bar.thick { height: 10px; }
  .bar.thin { height: 5px; }
  .headline {
    top: 806px; font-size: 86px; font-weight: 500;
    letter-spacing: 12px; color: var(--yellow);
  }
  .lineup {
    top: 933px; font-family: "Oswald", "Arial Narrow", sans-serif;
    font-size: 44px; font-weight: 700; color: var(--white); letter-spacing: 0;
  }
  .lineup .dot {
    display: inline-block; width: 11px; height: 11px; border-radius: 50%;
    background: var(--yellow); margin: 0 9px; vertical-align: middle; position: relative; top: -4px;
  }
  .subtitle-rule { position: absolute; height: 5px; background: var(--yellow); }
  .subtitle {
    top: 1014px; font-size: 34px; font-weight: 400;
    letter-spacing: 3px; color: var(--white);
  }
  .info {
    font-size: 29px; font-weight: 400; letter-spacing: 3px; color: var(--yellow);
  }
  .info.first { top: 1059px; }
  .info.second { top: 1105px; }
</style>
</head>
<body>
  <div class="centered event-date">12.00.15</div>
  <div class="centered doors">OPEN DOORS FROM 9:00 PM</div>

  <svg class="emblem" viewBox="0 0 512 512" aria-hidden="true">
    <defs>
      <radialGradient id="discFill" cx="50%" cy="45%" r="60%">
        <stop offset="0%" stop-color="#ffe23c"/>
        <stop offset="100%" stop-color="#f3ae12"/>
      </radialGradient>
    </defs>
    <circle cx="256" cy="256" r="250" fill="none" stroke="#f6c619" stroke-width="8"/>
    <circle cx="256" cy="256" r="221" fill="url(#discFill)"/>
  </svg>
  <svg class="emblem" viewBox="0 0 512 512" role="img" aria-label="Burst of scattered music notes around the venue name">
    <ellipse cx="256" cy="250" rx="150" ry="115" fill="#2a2410" opacity="0.18"/>
  </svg>
  <div class="centered venue-name">loudhall</div>

  <div class="bar thick" style="top:760px"></div>
  <div class="bar thin" style="top:777px"></div>

  <div class="centered headline">LIVE MUSIC GIGS</div>

  <div class="bar thick" style="top:881px"></div>
  <div class="bar thin" style="top:898px"></div>

  <div class="centered lineup">BANDS<span class="dot"></span>BANDS<span class="dot"></span>BANDS<span class="dot"></span>BANDS</div>

  <div class="bar thin" style="top:1000px"></div>
  <div class="subtitle-rule" style="left:124px; width:134px; top:1016px"></div>
  <div class="subtitle-rule" style="left:606px; width:138px; top:1016px"></div>
  <div class="subtitle-rule" style="left:124px; width:134px; top:1034px"></div>
  <div class="subtitle-rule" style="left:606px; width:138px; top:1034px"></div>
  <div class="centered subtitle">THIS IS A SUBTITLE TEXT</div>

  <div class="centered info first">WHERE YOU CAN WRITE SOME ADDITIONAL INFO</div>
  <div class="centered info second">ABOUT THE EVENT OR WRITE YOUR SOCIAL MEDIA LINKS</div>
</body>
</html>
```